Dental promotion

We are a family dental office that provides 99% of the dental service for the entire family, including IV sedation, wisdom teeth extraction, implant, Clearvanta, root canal, teeth whiting et cl. We currently have promotion for Clearvanta, implant and new patients who don’t have insurance. 1500 off Clearvanta, 2000 off for implant, 98 dollars for new patient that cover exam, x-ray, and regular cleaning. We also offer financing option.
More information please check our website
https://www.brookhollowfamilydentistry.example/

```html
<!DOCTYPE html>
<html lang="en">
<head>
<meta charset="utf-8">
<title>Brookhollow Family Dentistry – Postcard</title>
<link rel="stylesheet" href="https://fonts.googleapis.com/css2?family=Montserrat:wght@400;500;600;800&family=Poppins:ital,wght@0,400;0,500;0,600;0,700;1,400;1,700&display=swap">
<style>
  :root {
    --page-bg: #5f6b76;
    --deep-blue: #0594c6;
    --mid-blue: #19b4de;
    --cyan: #38d3ec;
    --bright-cyan: #3ddcf0;
    --hero-light: #9fd9e3;
    --ink: #1a1a1a;
    --white: #ffffff;
    --rule: #b5b5b5;
    --promo-blue: #0a7fc0;
  }
  * { box-sizing: border-box; margin: 0; padding: 0; }
  html, body { width: 875px; height: 1200px; overflow: hidden; }
  body {
    background: var(--page-bg);
    position: relative;
    font-family: "Poppins", sans-serif;
    color: var(--white);
  }
  .card {
    position: absolute;
    left: 73px;
    width: 729px;
    height: 486px;
    overflow: hidden;
    box-shadow: 0 10px 28px rgba(0,0,0,.35);
  }
  .card--front { top: 86px; }
  .card--back { top: 617px; background: var(--white); }
  .card svg.backdrop { position: absolute; inset: 0; }
  .abs { position: absolute; }

  /* Front */
  .logo-cap {
    left: 267px; top: -90px; width: 172px; height: 172px;
    border-radius: 50%; background: var(--white);
  }
  .logo-name {
    left: 267px; top: 40px; width: 172px; text-align: center;
    font-family: "Montserrat", sans-serif; font-weight: 600;
    font-size: 10.5px; line-height: 1.25; color: #2b2b2b;
  }
  .logo-name small { font-size: 5px; display: block; }
  .logo-dot {
    left: 347px; top: 20px; width: 12px; height: 12px; border-radius: 50%;
    background: var(--deep-blue);
  }
  .headline {
    left: 0; width: 729px; top: 346px; text-align: center;
    font-family: "Montserrat", sans-serif; font-weight: 800;
    font-size: 54px; line-height: 1; letter-spacing: -0.5px;
  }
  .lede {
    left: 40px; width: 649px; top: 410px; text-align: center;
    font-family: "Montserrat", sans-serif; font-weight: 400;
    font-size: 18px; line-height: 20px;
  }
  .tagline {
    left: 0; width: 729px; top: 456px; text-align: center;
    font-weight: 700; font-style: italic; font-size: 13.5px;
  }

  /* Back */
  .section-title { font-weight: 700; font-size: 19.5px; line-height: 1; }
  .about-copy { left: 27px; width: 268px; font-size: 8.2px; line-height: 9.5px; }
  .service { font-size: 14px; line-height: 15px; font-weight: 500; padding-left: 14px; }
  .service::before {
    content: ""; position: absolute; left: 0; top: 4px;
    width: 6px; height: 6px; border-radius: 50%; background: var(--white);
  }
  .promo {
    left: 28px; width: 226px; background: var(--white); border-radius: 6px;
    color: var(--promo-blue); font-weight: 700; text-align: center;
    display: flex; flex-direction: column; justify-content: center;
    letter-spacing: -0.5px;
  }
  .promo--big { height: 38px; font-size: 21px; }
  .promo--small { height: 42px; font-size: 14px; line-height: 14px; }
  .promo--small small { font-size: 10.5px; display: block; }
  .financing { left: 28px; top: 380px; font-style: italic; font-size: 12.5px; }
  .contact-title { left: 28px; top: 409px; color: var(--cyan); }
  .phone {
    left: 28px; top: 430px; font-size: 26px; font-weight: 700; line-height: 1;
    display: flex; align-items: center; gap: 8px;
  }
  .web { left: 28px; top: 462px; font-family: "Montserrat", sans-serif; font-size: 13px; }
  .stamp-box { left: 611px; top: 36px; width: 83px; height: 83px; border: 1px solid #888; }
  .address-rule { left: 399px; width: 295px; height: 1.5px; background: var(--rule); }
  .address {
    left: 427px; top: 422px; color: var(--ink);
    font-family: "Montserrat", sans-serif; font-size: 13px; line-height: 15px;
  }
  .divider { left: 579px; top: 418px; width: 2px; height: 48px; background: var(--cyan); }
  .review-badge { left: 602px; top: 420px; width: 92px; height: 42px; border-radius: 8px; background: #e8eef3; }
</style>
</head>
<body>

<section class="card card--front">
  <svg class="backdrop" width="729" height="486" viewBox="0 0 729 486">
    <defs>
      <linearGradient id="heroTone" x1="0" y1="0" x2="1" y2="1">
        <stop offset="0" stop-color="#18808f"/>
        <stop offset=".5" stop-color="var(--hero-light)"/>
        <stop offset="1" stop-color="#c9eef3"/>
      </linearGradient>
      <linearGradient id="panelTone" x1="0" y1="0" x2="0" y2="1">
        <stop offset="0" stop-color="#2fcbe7"/>
        <stop offset="1" stop-color="#12a8dc"/>
      </linearGradient>
    </defs>
    <rect width="729" height="330" fill="url(#heroTone)" role="img" aria-label="Photo: gloved hands sheltering a white model tooth"/>
    <polygon points="0,258 364,340 729,258 729,486 0,486" fill="url(#panelTone)"/>
    <polygon points="0,196 364,322 729,196 729,222 364,346 0,222" fill="#ffffff"/>
    <polygon points="0,440 85,486 0,486" fill="#22c6e4"/>
    <polygon points="729,440 640,486 729,486" fill="#22c6e4"/>
    <g stroke="#ffffff" stroke-width="6">
      <circle cx="61" cy="214" r="41" fill="#d9c6b8" role="img" aria-label="Photo: smiling man at a dental check"/>
      <circle cx="193" cy="248" r="52" fill="#8fc8dc" role="img" aria-label="Photo: girl having her teeth checked"/>
      <circle cx="369" cy="272" r="64" fill="#d8d2cb" role="img" aria-label="Photo: smiling woman in a dental chair"/>
      <circle cx="531" cy="248" r="52" fill="#9fc9e6" role="img" aria-label="Photo: boy at a dental exam"/>
      <circle cx="661" cy="214" r="41" fill="#d6c8c4" role="img" aria-label="Photo: woman receiving dental treatment"/>
    </g>
  </svg>
  <div class="abs logo-cap"></div>
  <div class="abs logo-dot"></div>
  <div class="abs logo-name">Brookhollow<br>Family Dentistry<small>M. CARTER, D.D.S., P.L.L.C.</small></div>
  <h1 class="abs headline">ALL UNDER ONE ROOF</h1>
  <p class="abs lede">We provide 99% of the services right here in our office including IV sedation, same day appointment!</p>
  <p class="abs tagline">Many of our patients appreciate the convenience and comfort of this approach.</p>
</section>

<section class="card card--back">
  <svg class="backdrop" width="729" height="486" viewBox="0 0 729 486">
    <defs>
      <linearGradient id="infoTone" x1="0" y1="0" x2="0.4" y2="1">
        <stop offset="0" stop-color="var(--deep-blue)"/>
        <stop offset="1" stop-color="#27c3e6"/>
      </linearGradient>
    </defs>
    <polygon points="348,0 384,0 318,262 373,486 340,486 283,262" fill="var(--bright-cyan)"/>
    <polygon points="0,0 348,0 283,262 340,486 0,486" fill="url(#infoTone)"/>
    <polygon points="0,403 319,403 340,486 0,486" fill="#000000"/>
    <path d="M405,432 a9,9 0 1 1 18,0 c0,7 -9,15 -9,15 c0,0 -9,-8 -9,-15z" fill="var(--cyan)" transform="translate(-6,-2)"/>
    <circle cx="408" cy="430" r="3" fill="#ffffff"/>
  </svg>

  <h2 class="abs section-title" style="left:27px;top:21px">About us:</h2>
  <p class="abs about-copy" style="top:46px">We are equipped with many new dental technologies: OptiScan scanner, Cone Beam CT 3D image scanner, et cl.</p>
  <p class="abs about-copy" style="top:72px">We are a local family dental office that has served surrounding area for more than 15 years. We provide affordable and excellent treatment.</p>

  <h2 class="abs section-title" style="left:27px;top:103px">Our services:</h2>
  <ul style="list-style:none">
    <li class="abs service" style="left:27px;top:131px">IV sedation</li>
    <li class="abs service" style="left:27px;top:157px">Wisdom teeth<br>extraction</li>
    <li class="abs service" style="left:27px;top:198px">Implant</li>
    <li class="abs service" style="left:154px;top:131px">teeth whiting</li>
    <li class="abs service" style="left:154px;top:157px">Clearvanta</li>
    <li class="abs service" style="left:154px;top:183px">root canal,</li>
  </ul>

  <div class="abs promo promo--big" style="top:229px">1500 off Clearvanta</div>
  <div class="abs promo promo--big" style="top:279px">2000 off for implant</div>
  <div class="abs promo promo--small" style="top:329px">98 dollars for new patient that<small>cover exam, x-ray, and regular cleaning</small></div>
  <p class="abs financing">We also offer financing option.</p>

  <h2 class="abs section-title contact-title">Contact us:</h2>
  <p class="abs phone">
    <svg width="20" height="20" viewBox="0 0 24 24" aria-hidden="true"><path d="M6.6 10.8a15 15 0 0 0 6.6 6.6l2.2-2.2a1 1 0 0 1 1-.25 11.4 11.4 0 0 0 3.6.57 1 1 0 0 1 1 1V20a1 1 0 0 1-1 1A17 17 0 0 1 3 4a1 1 0 0 1 1-1h3.5a1 1 0 0 1 1 1c0 1.25.2 2.45.57 3.6a1 1 0 0 1-.25 1z" fill="var(--cyan)"/></svg>
    919-555-0142
  </p>
  <p class="abs web">www.brookhollowfamilydentistry.example</p>

  <div class="abs stamp-box"></div>
  <div class="abs address-rule" style="top:167px"></div>
  <div class="abs address-rule" style="top:210px"></div>
  <div class="abs address-rule" style="top:252px"></div>
  <div class="abs address-rule" style="top:295px"></div>
  <div class="abs address-rule" style="top:340px"></div>

  <p class="abs address">4200 Alder Crest Way,<br>Suite #210 Maplewood,<br>NC 27599</p>
  <div class="abs divider"></div>
  <div class="abs review-badge" role="img" aria-label="Review listing badge"></div>
</section>

</body>
</html>
```